Looking for a PowerPoint design for a Pharmaceutical Company

We need a PowerPoint template design to be used company-wide. We are a pharmaceutical company with 63 years of history and want to use a new template design to work more efficiently and effectively. Below are some of the things we are looking for in the new template design.

- Simple, modern, and professional

- Practical for every day use (easy to read, easy to create)

- Slides will be mainly projected or viewed on screens, but should also work fine when printed. (e.g. We do not want to use up our inks / toners printing several pages..)

- It would be great if you could provide us a list of colors that can be effectively used in the slides. (e.g. for highlighting fonts / multiple graph colors / etc.)

- Just as an FYI, our current logo image is (dark) blue. I am not uploading the logo image here because we do not want you to be limited by the current logo image. Depending on the design, we may / may not put our logo image on the slides.

Please feel free to reach out to me if you have any questions. I look forward to seeing your design. Thank you!

Target Market(s)

Pharmaceutical industry. (To be used internally and externally)

Industry/Entity Type

Pharmaceutical

Font styles to use
Sans Serif

Requirements
Must have
• Title slide, Subtitle slide, graphs, charts, tables, bullet points, and any other slide style components normally included.
Nice to have
• - As we are in the pharma industry, we want the slides to give credibility. But we do not want it look "old", "boring", or "typical". Feel free to use unique / fresh colors.
Should not have
• - TOO many colors
• - Please do not use the images on our website, which contain faces. (Any image with faces in it...) They are stock images we bought for the website, and we do not want the images on our slides. (e.g. image of running woman on the main page, image of a surgeon, image of kids playing soccer, etc.)
• - We are not looking for a design that is a modified version of our website design. We are looking for something new.

```html
<!DOCTYPE html>
<html lang="en">
<head>
<meta charset="utf-8">
<title>Veltora Presentation Template</title>
<link href="https://fonts.googleapis.com/css2?family=Open+Sans:wght@400;600;700&display=swap" rel="stylesheet">
<style>
:root{
  --navy:#2b5486;
  --navy-dark:#1d3a63;
  --ink:#1f2d44;
  --light:#a9c7e6;
  --pale:#dfe9f4;
  --orange:#f2ab7c;
  --grey:#8b95a4;
  --bg:#eef1f5;
  --slide:#f8f9fb;
}
*{box-sizing:border-box;margin:0;padding:0}
html,body{width:912px;height:1200px;overflow:hidden;background:var(--bg);font-family:"Open Sans",sans-serif;color:var(--ink)}
.sheet{display:grid;grid-template-columns:repeat(3,298px);grid-template-rows:repeat(7,166px);gap:5px;padding:4px}
.slide{position:relative;background:var(--slide);overflow:hidden;box-shadow:0 1px 2px rgba(0,0,0,.12)}
.title{position:absolute;top:13px;left:0;right:0;text-align:center;font-size:8.5px;font-weight:700;letter-spacing:.2px}
.sub{position:absolute;top:24px;left:0;right:0;text-align:center;font-size:4px;color:var(--grey)}
.foot{position:absolute;left:6px;right:6px;bottom:5px;height:6px;display:flex;align-items:center;justify-content:space-between}
.brand{display:flex;align-items:center;gap:2px;font-size:4.5px;font-weight:700;color:var(--navy)}
.brand i{width:4px;height:4px;border-radius:50%;background:var(--navy);display:block}
.dots{display:flex;gap:1.5px;align-items:center}
.dots b{width:4px;height:3px;display:block}
.dots b:nth-child(1){background:var(--navy)}
.dots b:nth-child(2){background:var(--light)}
.dots b:nth-child(3){background:#c9d2dc}
.dots b:nth-child(4){background:#b9d3a8}
.dots b:nth-child(5){background:var(--navy-dark)}
.dots b:nth-child(6){background:var(--navy-dark)}
.dots span{background:var(--navy);color:#fff;font-size:3.5px;width:6px;height:6px;display:flex;align-items:center;justify-content:center;margin-left:2px}
.lo{font-size:3.7px;line-height:1.4;color:var(--grey)}
.hd{font-size:7.5px;font-weight:600;color:var(--navy);line-height:1.3}
.lbl{font-size:4.2px;font-weight:700;color:var(--ink)}
.photo{position:absolute}
.abs{position:absolute}
.white{color:#fff}
.circ{width:12px;height:12px;border-radius:50%;display:flex;align-items:center;justify-content:center}
.toc-row{display:flex;align-items:center;gap:5px;font-size:4.3px;font-weight:600;height:20px}
.toc-row .n{width:12px;height:12px;border-radius:50%;background:var(--navy);color:#fff;font-size:3.5px;display:flex;align-items:center;justify-content:center}
.bul{display:flex;gap:3px}
.bul::before{content:"";width:3px;height:3px;border-radius:50%;background:var(--navy);margin-top:1px;flex:none}
</style>
</head>
<body>
<main class="sheet">

<!-- 1 Title -->
<section class="slide">
  <div class="photo" role="img" aria-label="Company headquarters building" style="left:0;top:0;width:170px;height:134px;background:linear-gradient(160deg,#dfe4ea,#9aa5b2 60%,#c7ced6)"></div>
  <div class="abs" style="left:178px;top:62px;border-left:1px solid var(--navy);padding-left:5px">
    <div style="font-size:7.5px;font-weight:700;color:var(--navy)">PRESENTATION TITLE HERE</div>
    <div style="font-size:4.5px;color:var(--orange)">Title Page</div>
  </div>
  <div class="abs" style="left:0;right:0;bottom:0;height:32px;background:#fff"></div>
  <div class="abs" style="left:10px;bottom:6px">
    <div style="font-size:3.8px;color:var(--grey)">Presented by</div>
    <div style="font-size:8px;color:var(--navy)">Mr. Daniel Reyes</div>
    <div style="font-size:3.8px;color:var(--grey)">Friday, July 8, 2016</div>
  </div>
  <div class="brand abs" style="right:10px;bottom:10px;font-size:7.5px"><i style="width:7px;height:7px"></i>Veltora</div>
</section>

<!-- 2 Subtitle -->
<section class="slide">
  <div class="photo" role="img" aria-label="Gloved hands holding a vial in a laboratory" style="inset:0;background:linear-gradient(135deg,#5e6570,#c9ccd1 55%,#8f949b)"></div>
  <div class="abs" style="left:0;top:112px;width:118px;height:30px;background:rgba(43,84,134,.9);padding:6px 0 0 26px">
    <div style="font-size:7px;font-weight:700;color:#fff;border-left:1px solid #fff;padding-left:4px">SUB TITLE HERE
      <div style="font-size:4.3px;font-weight:400;color:var(--orange)">Subtitle Page</div></div>
  </div>
</section>

<!-- 3 TOC -->
<section class="slide">
  <div class="title">TABLE OF CONTENTS</div><div class="sub">Your Subtitle Here</div>
  <div class="abs" style="left:36px;top:44px">
    <div class="toc-row"><span class="n">01</span>YOUR CONTENT NUMBER 0 HERE</div>
    <div class="toc-row"><span class="n">02</span>YOUR CONTENT NUMBER 0 HERE</div>
    <div class="toc-row"><span class="n">03</span>YOUR CONTENT NUMBER 0 HERE</div>
    <div class="toc-row"><span class="n">04</span>YOUR CONTENT NUMBER 0 HERE</div>
    <div class="toc-row"><span class="n">05</span>YOUR CONTENT NUMBER 0 HERE</div>
  </div>
  <div class="abs" style="left:161px;top:44px">
    <div class="toc-row"><span class="n">06</span>YOUR CONTENT NUMBER 0 HERE</div>
    <div class="toc-row"><span class="n">07</span>YOUR CONTENT NUMBER 0 HERE</div>
    <div class="toc-row"><span class="n">08</span>YOUR CONTENT NUMBER 0 HERE</div>
    <div class="toc-row"><span class="n">09</span>YOUR CONTENT NUMBER 0 HERE</div>
    <div class="toc-row"><span class="n">10</span>YOUR CONTENT NUMBER 0 HERE</div>
  </div>
  <div class="foot"><div class="brand"><i></i>Veltora</div><div class="dots"><b></b><b></b><b></b><b></b><b></b><span>3</span></div></div>
</section>

<!-- 4 Vision -->
<section class="slide">
  <div class="title">OUR VISION &amp; MISSION</div><div class="sub">Your Subtitle Here</div>
  <div class="abs" role="img" aria-label="Blue toned laboratory backdrop" style="left:0;right:0;top:38px;height:108px;background:linear-gradient(90deg,#2b5486,#34608f)"></div>
  <div class="abs white" style="left:20px;top:66px;width:120px">
    <div style="font-size:7px;font-weight:600;line-height:1.35">Go to the Next Level<br>Without look in the past</div>
    <div class="lo" style="color:#d5e2f0;margin-top:6px">Lorem ipsum dolor sit amet, consectetur adipiscing elit, sed do eiusmod tempor incididunt ut labore et dolore magna aliqua.</div>
  </div>
  <div class="abs white" style="left:174px;top:56px;font-size:4px">Our Mission :</div>
  <div class="abs" style="left:174px;top:66px;display:grid;gap:8px">
    <div style="display:flex;gap:5px;align-items:center"><div class="circ" style="background:#fff"><svg width="6" height="6" viewBox="0 0 10 10"><circle cx="5" cy="5" r="3" fill="none" stroke="#2b5486" stroke-width="1.5"/></svg></div><div class="white" style="font-size:3.3px;line-height:1.35"><b>YOUR TEXT HERE</b><br>Lorem ipsum dolor sit<br>consectetur adipiscing elit, sed do eiusmod tempo.</div></div>
    <div style="display:flex;gap:5px;align-items:center"><div class="circ" style="background:#fff"><svg width="6" height="6" viewBox="0 0 10 10"><path d="M5 9L1 5a2.2 2.2 0 014-3 2.2 2.2 0 014 3z" fill="#2b5486"/></svg></div><div class="white" style="font-size:3.3px;line-height:1.35"><b>YOUR TEXT HERE</b><br>Lorem ipsum dolor sit<br>consectetur adipiscing elit, sed do eiusmod tempo.</div></div>
    <div style="display:flex;gap:5px;align-items:center"><div class="circ" style="background:#fff"><svg width="6" height="6" viewBox="0 0 10 10"><path d="M2 1h6L2 9h6z" fill="none" stroke="#2b5486" stroke-width="1.3"/></svg></div><div class="white" style="font-size:3.3px;line-height:1.35"><b>YOUR TEXT HERE</b><br>Lorem ipsum dolor sit<br>consectetur adipiscing elit, sed do eiusmod tempo.</div></div>
  </div>
  <div class="foot"><div class="brand"><i></i>Veltora</div><div class="dots"><b></b><b></b><b></b><b></b><b></b><span>4</span></div></div>
</section>

<!-- 5 Single description -->
<section class="slide">
  <div class="title">SINGLE DESCRIPTION</div><div class="sub">Your Subtitle Here</div>
  <div class="abs" style="left:26px;top:50px;right:26px">
    <div class="hd">We are Veltora<br>Building a Healthier Future Together</div>
    <p class="lo" style="margin-top:8px">Lorem ipsum dolor sit amet, consectetur adipiscing elit, sed do eiusmod tempor incididunt ut labore et dolore magna aliqua. Ut enim ad minim veniam, quis nostrud exercitation ullamco laboris nisi ut aliquip ex ea commodo consequat.</p>
    <p class="lo" style="margin-top:5px">Duis aute irure dolor in reprehenderit in voluptate velit esse cillum dolore eu fugiat nulla pariatur. Excepteur sint occaecat cupidatat non proident, sunt in culpa qui officia deserunt mollit anim id est laborum.</p>
    <p class="lo" style="margin-top:5px">Ut enim ad minim veniam, quis nostrud exercitation ullamco laboris nisi ut aliquip ex ea commodo consequat.</p>
  </div>
  <div class="foot"><div class="brand"><i></i>Veltora</div><div class="dots"><b></b><b></b><b></b><b></b><b></b><span>5</span></div></div>
</section>

<!-- 6 Quote -->
<section class="slide">
  <div class="photo" role="img" aria-label="Blue toned company lobby" style="inset:0;background:linear-gradient(180deg,#34608f,#2b5486)"></div>
  <div class="abs white" style="left:0;right:0;top:10px;text-align:center;font-size:6px;font-weight:700;opacity:.25">VELTORA PHARMA CO.</div>
  <div class="abs" style="left:136px;top:48px;width:26px;height:26px;border-radius:50%;background:#8fb4da;display:flex;align-items:center;justify-content:center;color:#fff;font-size:16px;font-weight:700;line-height:1">“</div>
  <div class="abs white" style="left:0;right:0;top:84px;text-align:center;font-size:7.5px;line-height:1.4">Wherever the art of medicine is loved,<br>there is also a love of humanity.</div>
  <div class="abs" style="left:0;right:0;top:115px;text-align:center;font-size:3.8px;color:#c9d8ea">- Ancient Proverb -</div>
</section>

<!-- 7 Numbering 1 -->
<section class="slide">
  <div class="title">NUMBERING 1 LEVEL</div><div class="sub">Your Subtitle Here</div>
  <div class="abs" style="left:22px;top:50px;display:grid;grid-template-columns:repeat(3,89px);row-gap:12px">
    <div style="display:flex;gap:4px"><div style="font-size:13px;color:var(--navy);border-right:1px solid var(--light);padding-right:4px;height:34px">1</div><div><div class="lbl" style="color:var(--navy)">YOUR TEXT HERE</div><div class="lo">Lorem ipsum<br>consectetur adipiscing<br>elit, dolor sit sed do<br>eiusmod tempo.</div></div></div>
    <div style="display:flex;gap:4px"><div style="font-size:13px;color:var(--navy);border-right:1px solid var(--light);padding-right:4px;height:34px">2</div><div><div class="lbl" style="color:var(--navy)">YOUR TEXT HERE</div><div class="lo">Lorem ipsum<br>consectetur adipiscing<br>elit, dolor sit sed do<br>eiusmod tempo.</div></div></div>
    <div style="display:flex;gap:4px"><div style="font-size:13px;color:var(--navy);border-right:1px solid var(--light);padding-right:4px;height:34px">3</div><div><div class="lbl" style="color:var(--navy)">YOUR TEXT HERE</div><div class="lo">Lorem ipsum<br>consectetur adipiscing<br>elit, dolor sit sed do<br>eiusmod tempo.</div></div></div>
    <div style="display:flex;gap:4px"><div style="font-size:13px;color:var(--navy);border-right:1px solid var(--light);padding-right:4px;height:34px">4</div><div><div class="lbl" style="color:var(--navy)">YOUR TEXT HERE</div><div class="lo">Lorem ipsum<br>consectetur adipiscing<br>elit, dolor sit sed do<br>eiusmod tempo.</div></div></div>
    <div style="display:flex;gap:4px"><div style="font-size:13px;color:var(--navy);border-right:1px solid var(--light);padding-right:4px;height:34px">5</div><div><div class="lbl" style="color:var(--navy)">YOUR TEXT HERE</div><div class="lo">Lorem ipsum<br>consectetur adipiscing<br>elit, dolor sit sed do<br>eiusmod tempo.</div></div></div>
    <div style="display:flex;gap:4px"><div style="font-size:13px;color:var(--navy);border-right:1px solid var(--light);padding-right:4px;height:34px">6</div><div><div class="lbl" style="color:var(--navy)">YOUR TEXT HERE</div><div class="lo">Lorem ipsum<br>consectetur adipiscing<br>elit, dolor sit sed do<br>eiusmod tempo.</div></div></div>
  </div>
  <div class="foot"><div class="brand"><i></i>Veltora</div><div class="dots"><b></b><b></b><b></b><b></b><b></b><span>7</span></div></div>
</section>

<!-- 8 Divider -->
<section class="slide">
  <div class="photo" role="img" aria-label="Blue toned factory building" style="inset:0;background:linear-gradient(180deg,#3a6594,#2b5486 70%,#4a72a0)"></div>
  <div class="abs white" style="left:0;right:0;top:45px;text-align:center">
    <div style="font-size:4px">DIVIDER PAGE</div>
    <div style="font-size:9px;font-weight:700">YOUR TITLE HERE</div>
    <div style="font-size:5px;color:#d2e0ef">Your Subtitle Here</div>
  </div>
</section>

<!-- 9 Numbering 2 -->
<section class="slide">
  <div class="title">NUMBERING 2 LEVEL</div><div class="sub">Your Subtitle Here</div>
  <div class="abs" style="left:26px;top:50px;display:grid;grid-template-columns:140px 120px;row-gap:10px">
    <div><div class="lbl"><span style="font-weight:400">1 &nbsp;|</span> YOUR TEXT HERE</div><div class="lo" style="padding-left:10px;margin-top:3px">• Lorem ipsumconsectetur adipiscing elit, dolor sit sed do eiusmod tempo.<br>• Lorem ipsumconsectetur adipiscing elit, dolor sit sed do eiusmod tempo.</div></div>
    <div><div class="lbl"><span style="font-weight:400">2 &nbsp;|</span> YOUR TEXT HERE</div><div class="lo" style="padding-left:10px;margin-top:3px">• Lorem ipsumconsectetur adipiscing elit, dolor sit sed do eiusmod tempo.<br>• Lorem ipsumconsectetur adipiscing elit, dolor sit sed do eiusmod tempo.</div></div>
    <div><div class="lbl"><span style="font-weight:400">3 &nbsp;|</span> YOUR TEXT HERE</div><div class="lo" style="padding-left:10px;margin-top:3px">• Lorem ipsumconsectetur adipiscing elit, dolor sit sed do eiusmod tempo.<br>• Lorem ipsumconsectetur adipiscing elit, dolor sit sed do eiusmod tempo.</div></div>
    <div><div class="lbl"><span style="font-weight:400">4 &nbsp;|</span> YOUR TEXT HERE</div><div class="lo" style="padding-left:10px;margin-top:3px">• Lorem ipsumconsectetur adipiscing elit, dolor sit sed do eiusmod tempo.<br>• Lorem ipsumconsectetur adipiscing elit, dolor sit sed do eiusmod tempo.</div></div>
  </div>
  <div class="foot"><div class="brand"><i></i>Veltora</div><div class="dots"><b></b><b></b><b></b><b></b><b></b><span>9</span></div></div>
</section>

<!-- 10 Quote today -->
<section class="slide">
  <div class="photo" role="img" aria-label="Hands holding a four-leaf clover seedling" style="left:34px;top:0;width:118px;height:166px;background:linear-gradient(180deg,#f2f3f4,#dfe3de 50%,#c8d4bf)"></div>
  <div class="abs" style="left:160px;right:10px;top:48px;text-align:center">
    <div style="font-size:8px;font-weight:700">OUR QUOTE TODAY</div>
    <div style="font-size:5.3px;color:var(--grey);margin-top:18px;line-height:1.45">Natural forces within us are the true<br>healers of disease.</div>
    <div style="font-size:3.6px;color:var(--grey);margin-top:6px">- Ancient Proverb -</div>
    <div style="font-size:12px;color:var(--light);margin-top:4px">”</div>
  </div>
  <div class="foot"><div class="brand"><i></i>Veltora</div><div class="dots"><b></b><b></b><b></b><b></b><b></b><span>10</span></div></div>
</section>

<!-- 11 Three column -->
<section class="slide">
  <div class="title">THREE COLUMN DESCRIPTION</div><div class="sub">Your Subtitle Here</div>
  <div class="abs" style="left:26px;top:50px"><div class="hd">We are Veltora<br>Building a Healthier Future Together</div></div>
  <div class="abs" style="left:26px;right:22px;top:80px;display:grid;grid-template-columns:repeat(3,1fr);gap:10px">
    <div class="lo">Lorem ipsum dolor sit amet, consectetur adipiscing elit, sed do eiusmod tempor incididunt ut labore et dolore magna aliqua.<br><br>Ut enimad minim veniam, quis nostrud exercitation ullamco laboris nisi ut aliquip ex ea commodo consequat.</div>
    <div class="lo">Lorem ipsum dolor sit amet, consectetur adipiscing elit, sed do eiusmod tempor incididunt ut labore et dolore magna aliqua.<br><br>Ut enimad minim veniam, quis nostrud exercitation ullamco laboris nisi ut aliquip ex ea commodo consequat.</div>
    <div class="lo">Lorem ipsum dolor sit amet, consectetur adipiscing elit, sed do eiusmod tempor incididunt ut labore et dolore magna aliqua.<br><br>Ut enimad minim veniam, quis nostrud exercitation ullamco laboris nisi ut aliquip ex ea commodo consequat.</div>
  </div>
  <div class="foot"><div class="brand"><i></i>Veltora</div><div class="dots"><b></b><b></b><b></b><b></b><b></b><span>11</span></div></div>
</section>

<!-- 12 Who we are -->
<section class="slide">
  <div class="title">WHO WE ARE</div><div class="sub">Your Subtitle Here</div>
  <div class="photo" role="img" aria-label="Lab technician in protective clothing" style="left:23px;top:41px;width:120px;height:103px;background:linear-gradient(135deg,#dde6ef,#a9bfd6 60%,#7d98b6)"></div>
  <div class="abs" style="left:162px;right:18px;top:50px">
    <div class="hd">We are Veltora<br>Building a Healthier<br>Future Together</div>
    <p class="lo" style="margin-top:7px">Lorem ipsum dolor sit amet, consectetur adipiscing elit, sed do eiusmod tempor incididunt ut labore et dolore magna aliqua.</p>
    <p class="lo" style="margin-top:5px">Ut enimad minim veniam, quis nostrud exercitation ullamco laboris nisi ut aliquip ex ea commodo consequat.</p>
  </div>
  <div class="foot"><div class="brand"><i></i>Veltora</div><div class="dots"><b></b><b></b><b></b><b></b><b></b><span>12</span></div></div>
</section>

<!-- 13 Bullets 1 -->
<section class="slide">
  <div class="title">BULLETS POINT 1 LEVEL</div><div class="sub">Your Subtitle Here</div>
  <div class="abs" style="left:24px;top:54px;display:grid;grid-template-columns:repeat(3,89px);row-gap:14px">
    <div class="bul"><div><div class="lbl">YOUR TEXT HERE</div><div class="lo">Lorem ipsum dolor sit<br>consectetur adipiscing elit,<br>sed do eiusmod tempo.</div></div></div>
    <div class="bul"><div><div class="lbl">YOUR TEXT HERE</div><div class="lo">Lorem ipsum dolor sit<br>consectetur adipiscing elit,<br>sed do eiusmod tempo.</div></div></div>
    <div class="bul"><div><div class="lbl">YOUR TEXT HERE</div><div class="lo">Lorem ipsum dolor sit<br>consectetur adipiscing elit,<br>sed do eiusmod tempo.</div></div></div>
    <div class="bul"><div><div class="lbl">YOUR TEXT HERE</div><div class="lo">Lorem ipsum dolor sit<br>consectetur adipiscing elit,<br>sed do eiusmod tempo.</div></div></div>
    <div class="bul"><div><div class="lbl">YOUR TEXT HERE</div><div class="lo">Lorem ipsum dolor sit<br>consectetur adipiscing elit,<br>sed do eiusmod tempo.</div></div></div>
    <div class="bul"><div><div class="lbl">YOUR TEXT HERE</div><div class="lo">Lorem ipsum dolor sit<br>consectetur adipiscing elit,<br>sed do eiusmod tempo.</div></div></div>
  </div>
  <div class="foot"><div class="brand"><i></i>Veltora</div><div class="dots"><b></b><b></b><b></b><b></b><b></b><span>13</span></div></div>
</section>

<!-- 14 Services -->
<section class="slide">
  <div class="title">OUR SERVICES</div><div class="sub">Your Subtitle Here</div>
  <div class="abs" style="left:23px;top:57px;display:grid;grid-template-columns:repeat(4,55px);gap:11px">
    <div style="height:73px;background:var(--pale);text-align:center;padding-top:14px"><div class="circ" style="background:#fff;margin:0 auto"><svg width="6" height="6" viewBox="0 0 10 10"><path d="M5 9L1 5a2.2 2.2 0 014-3 2.2 2.2 0 014 3z" fill="#2b5486"/></svg></div><div style="font-size:3.3px;font-weight:700;margin-top:13px">YOUR TEXT HERE</div><div class="lo" style="font-size:3px">Lorem ipsum dolor<br>sit consectetur<br>adipiscing elit.</div></div>
    <div style="height:73px;background:var(--navy);text-align:center;padding-top:14px;color:#fff"><div class="circ" style="background:#fff;margin:0 auto"><svg width="6" height="6" viewBox="0 0 10 10"><circle cx="5" cy="5" r="3" fill="none" stroke="#2b5486" stroke-width="1.5"/></svg></div><div style="font-size:3.3px;font-weight:700;margin-top:13px">YOUR TEXT HERE</div><div class="lo" style="font-size:3px;color:#d5e2f0">Lorem ipsum dolor<br>sit consectetur<br>adipiscing elit.</div></div>
    <div style="height:73px;background:var(--pale);text-align:center;padding-top:14px"><div class="circ" style="background:#fff;margin:0 auto"><svg width="6" height="6" viewBox="0 0 10 10"><path d="M2 1h6L2 9h6z" fill="none" stroke="#2b5486" stroke-width="1.3"/></svg></div><div style="font-size:3.3px;font-weight:700;margin-top:13px">YOUR TEXT HERE</div><div class="lo" style="font-size:3px">Lorem ipsum dolor<br>sit consectetur<br>adipiscing elit.</div></div>
    <div style="height:73px;background:var(--pale);text-align:center;padding-top:14px"><div class="circ" style="background:#fff;margin:0 auto"><svg width="6" height="6" viewBox="0 0 10 10"><path d="M5 1l4 4H6v4H4V5H1z" fill="#2b5486"/></svg></div><div style="font-size:3.3px;font-weight:700;margin-top:13px">YOUR TEXT HERE</div><div class="lo" style="font-size:3px">Lorem ipsum dolor<br>sit consectetur<br>adipiscing elit.</div></div>
  </div>
  <div class="foot"><div class="brand"><i></i>Veltora</div><div class="dots"><b></b><b></b><b></b><b></b><b></b><span>14</span></div></div>
</section>

<!-- 15 Bullets 2 -->
<section class="slide">
  <div class="title">BULLETS POINT 2 LEVEL</div><div class="sub">Your Subtitle Here</div>
  <div class="abs" style="left:24px;top:48px;display:grid;grid-template-columns:145px 120px;row-gap:10px">
    <div><div class="bul lbl">YOUR TEXT HERE</div><div class="lo" style="padding-left:10px;margin-top:3px">• Lorem ipsumconsectetur adipiscing elit, dolor sit sed do eiusmod tempo.<br>• Lorem ipsumconsectetur adipiscing elit, dolor sit sed do eiusmod tempo.</div></div>
    <div><div class="bul lbl">YOUR TEXT HERE</div><div class="lo" style="padding-left:10px;margin-top:3px">• Lorem ipsumconsectetur adipiscing elit, dolor sit sed do eiusmod tempo.<br>• Lorem ipsumconsectetur adipiscing elit, dolor sit sed do eiusmod tempo.</div></div>
    <div><div class="bul lbl">YOUR TEXT HERE</div><div class="lo" style="padding-left:10px;margin-top:3px">• Lorem ipsumconsectetur adipiscing elit, dolor sit sed do eiusmod tempo.<br>• Lorem ipsumconsectetur adipiscing elit, dolor sit sed do eiusmod tempo.</div></div>
    <div><div class="bul lbl">YOUR TEXT HERE</div><div class="lo" style="padding-left:10px;margin-top:3px">• Lorem ipsumconsectetur adipiscing elit, dolor sit sed do eiusmod tempo.<br>• Lorem ipsumconsectetur adipiscing elit, dolor sit sed do eiusmod tempo.</div></div>
  </div>
  <div class="foot"><div class="brand"><i></i>Veltora</div><div class="dots"><b></b><b></b><b></b><b></b><b></b><span>15</span></div></div>
</section>

<!-- 16 Bar chart -->
<section class="slide">
  <div class="title">BAR CHART AREA</div><div class="sub">Your Subtitle Here</div>
  <svg class="abs" style="left:16px;top:54px" width="120" height="82" viewBox="0 0 120 82">
    <g font-size="3" fill="#8b95a4" font-family="Open Sans, sans-serif">
      <text x="0" y="5">5</text><text x="0" y="21">4</text><text x="0" y="37">3</text><text x="0" y="53">2</text><text x="0" y="69">1</text>
      <text x="18" y="76">Category 1</text><text x="55" y="76">Category 2</text><text x="92" y="76">Category 3</text>
      <text x="20" y="81">■ Series 1  ■ Series 2  ■ Series 3</text>
    </g>
    <line x1="6" y1="70" x2="118" y2="70" stroke="#c9d2dc" stroke-width=".4"/>
    <rect x="24" y="40" width="5" height="30" fill="#2b5486"/><rect x="30" y="55" width="5" height="15" fill="#f2ab7c"/><rect x="36" y="58" width="5" height="12" fill="#a9c7e6"/>
    <rect x="61" y="55" width="5" height="15" fill="#2b5486"/><rect x="67" y="34" width="5" height="36" fill="#f2ab7c"/><rect x="73" y="58" width="5" height="12" fill="#a9c7e6"/>
    <rect x="98" y="43" width="5" height="27" fill="#2b5486"/><rect x="104" y="52" width="5" height="18" fill="#f2ab7c"/><rect x="110" y="40" width="5" height="30" fill="#a9c7e6"/>
  </svg>
  <div class="abs" style="left:162px;right:16px;top:52px">
    <div class="hd">We are Veltora<br>Building a Healthier<br>Future Together</div>
    <p class="lo" style="margin-top:6px">Lorem ipsum dolor sit amet, consectetur adipiscing elit, sed do eiusmod tempor incididunt ut labore et dolore magna aliqua.</p>
    <p class="lo" style="margin-top:5px">Ut enimad minim veniam, quis nostrud exercitation ullamco laboris nisi ut aliquip ex ea commodo consequat.</p>
  </div>
  <div class="foot"><div class="brand"><i></i>Veltora</div><div class="dots"><b></b><b></b><b></b><b></b><b></b><span>16</span></div></div>
</section>

<!-- 17 Chart -->
<section class="slide">
  <div class="title">CHART AREA</div><div class="sub">Your Subtitle Here</div>
  <svg class="abs" style="left:36px;top:52px" width="80" height="88" viewBox="0 0 80 88">
    <text x="30" y="4" font-size="4" fill="#1f2d44" font-family="Open Sans, sans-serif">Sales</text>
    <g transform="translate(38,42)" fill="none" stroke-width="7">
      <circle r="28" stroke="#a9c7e6"/>
      <circle r="28" stroke="#2b5486" stroke-dasharray="103 176" transform="rotate(-90)"/>
      <circle r="28" stroke="#f2ab7c" stroke-dasharray="14 176" stroke-dashoffset="-150" transform="rotate(-90)"/>
      <circle r="28" stroke="#b9d3a8" stroke-dasharray="12 176" stroke-dashoffset="-164" transform="rotate(-90)"/>
    </g>
    <text x="4" y="86" font-size="2.8" fill="#8b95a4" font-family="Open Sans, sans-serif">● 1st Qtr  ● 2nd Qtr  ● 3rd Qtr  ● 4th Qtr</text>
  </svg>
  <div class="abs" style="left:152px;top:55px;display:grid;gap:9px">
    <div style="display:flex;gap:5px"><div class="circ" style="border:1px solid var(--light)"><svg width="6" height="6" viewBox="0 0 10 10"><circle cx="5" cy="5" r="3" fill="none" stroke="#2b5486" stroke-width="1.5"/></svg></div><div style="font-size:3.3px;line-height:1.35"><b>YOUR TEXT HERE</b><div class="lo" style="font-size:3.3px">Lorem ipsum dolor sit<br>consectetur adipiscing elit, sed do eiusmod<br>tempo.</div></div></div>
    <div style="display:flex;gap:5px"><div class="circ" style="border:1px solid var(--light)"><svg width="6" height="6" viewBox="0 0 10 10"><path d="M5 9L1 5a2.2 2.2 0 014-3 2.2 2.2 0 014 3z" fill="#2b5486"/></svg></div><div style="font-size:3.3px;line-height:1.35"><b>YOUR TEXT HERE</b><div class="lo" style="font-size:3.3px">Lorem ipsum dolor sit<br>consectetur adipiscing elit, sed do eiusmod<br>tempo.</div></div></div>
    <div style="display:flex;gap:5px"><div class="circ" style="border:1px solid var(--light)"><svg width="6" height="6" viewBox="0 0 10 10"><path d="M2 1h6L2 9h6z" fill="none" stroke="#2b5486" stroke-width="1.3"/></svg></div><div style="font-size:3.3px;line-height:1.35"><b>YOUR TEXT HERE</b><div class="lo" style="font-size:3.3px">Lorem ipsum dolor sit<br>consectetur adipiscing elit, sed do eiusmod<br>tempo.</div></div></div>
  </div>
  <div class="foot"><div class="brand"><i></i>Veltora</div><div class="dots"><b></b><b></b><b></b><b></b><b></b><span>17</span></div></div>
</section>

<!-- 18 Table -->
<section class="slide">
  <div class="title">TABLE AREA</div><div class="sub">Your Subtitle Here</div>
  <div class="abs" style="left:47px;top:46px;width:204px;display:grid;grid-template-columns:82px 61px 61px;font-size:3px">
    <div style="background:var(--navy-dark);color:#fff;height:26px;padding:8px 4px;font-weight:700">Description</div>
    <div style="background:var(--light);color:#fff;height:26px;padding:4px;text-align:center;font-weight:700">Column 1</div>
    <div style="background:var(--orange);color:#fff;height:26px;padding:4px;text-align:center;font-weight:700">Column 2</div>
    <div style="background:#fff;padding:4px;line-height:2.3;color:var(--grey)">Description 1<br>Description 2<br>Description 3<br>Description 4<br>Description 5<br>Description 6<br>Description 7<br>Description 8</div>
    <div style="background:#fff;padding:4px;line-height:2.3;text-align:center;border-left:1px solid var(--pale)">●<br>●<br>&nbsp;<br>●<br>Text Column 1<br>&nbsp;<br>Text Column 1<br>●</div>
    <div style="background:#fff;padding:4px;line-height:2.3;text-align:center;border-left:1px solid var(--pale)">●<br>●<br>●<br>●<br>Text Column 2<br>&nbsp;<br>Text Column 2<br>●</div>
  </div>
  <div class="foot"><div class="brand"><i></i>Veltora</div><div class="dots"><b></b><b></b><b></b><b></b><b></b><span>18</span></div></div>
</section>

<!-- 19 Two column -->
<section class="slide">
  <div class="title">TWO COLUMN DESCRIPTION</div><div class="sub">Your Subtitle Here</div>
  <div class="abs" style="left:26px;top:50px"><div class="hd">We are Veltora<br>Building a Healthier Future Together</div></div>
  <div class="abs" style="left:26px;right:22px;top:80px;display:grid;grid-template-columns:1fr 1fr;gap:16px">
    <div class="lo">Lorem ipsum dolor sit amet, consectetur adipiscing elit, sed do eiusmod tempor incididunt ut labore et dolore magna aliqua.<br><br>Ut enimad minim veniam, quis nostrud exercitation ullamco laboris nisi ut aliquip ex ea commodo consequat.</div>
    <div class="lo">Lorem ipsum dolor sit amet, consectetur adipiscing elit, sed do eiusmod tempor incididunt ut labore et dolore magna aliqua.<br><br>Ut enimad minim veniam, quis nostrud exercitation ullamco laboris nisi ut aliquip ex ea commodo consequat.</div>
  </div>
  <div class="foot"><div class="brand"><i></i>Veltora</div><div class="dots"><b></b><b></b><b></b><b></b><b></b><span>19</span></div></div>
</section>

<!-- 20 Clients -->
<section class="slide">
  <div class="title">OUR CLIENTS SAY</div><div class="sub">Your Subtitle Here</div>
  <div class="abs" style="left:22px;top:45px;display:grid;grid-template-columns:137px 120px;row-gap:12px">
    <div style="display:flex;gap:6px"><div role="img" aria-label="Client portrait" style="width:30px;height:30px;border-radius:50%;background:#b8c2cd;flex:none"></div><div style="font-size:3.3px;line-height:1.4"><b>MR. CLARK CENT</b><div style="color:var(--light)">Hospital Manager</div><div class="lo" style="font-size:3.3px">consectetur adipiscing elit, sed do eiusmod tempo.</div><div style="font-size:9px;color:var(--light);text-align:right;line-height:.8">”</div></div></div>
    <div style="display:flex;gap:6px"><div role="img" aria-label="Client portrait" style="width:30px;height:30px;border-radius:50%;background:#b8c2cd;flex:none"></div><div style="font-size:3.3px;line-height:1.4"><b>MR. RICH ZONE</b><div style="color:var(--orange)">Private Investor</div><div class="lo" style="font-size:3.3px">consectetur adipiscing elit, sed do eiusmod tempo.</div><div style="font-size:9px;color:var(--light);text-align:right;line-height:.8">”</div></div></div>
    <div style="display:flex;gap:6px"><div role="img" aria-label="Client portrait" style="width:30px;height:30px;border-radius:50%;background:#b8c2cd;flex:none"></div><div style="font-size:3.3px;line-height:1.4"><b>MR. BIG GROW</b><div style="color:var(--orange)">Surgeon</div><div class="lo" style="font-size:3.3px">consectetur adipiscing elit, sed do eiusmod tempo.</div><div style="font-size:9px;color:var(--light);text-align:right;line-height:.8">”</div></div></div>
    <div style="display:flex;gap:6px"><div role="img" aria-label="Client portrait" style="width:30px;height:30px;border-radius:50%;background:#b8c2cd;flex:none"></div><div style="font-size:3.3px;line-height:1.4"><b>MR. JOHN DOE</b><div style="color:var(--light)">Hospital Administrator</div><div class="lo" style="font-size:3.3px">consectetur adipiscing elit, sed do eiusmod tempo.</div><div style="font-size:9px;color:var(--light);text-align:right;line-height:.8">”</div></div></div>
  </div>
  <div class="foot"><div class="brand"><i></i>Veltora</div><div class="dots"><b></b><b></b><b></b><b></b><b></b><span>20</span></div></div>
</section>

<!-- 21 Thank you -->
<section class="slide" style="background:var(--navy-dark)">
  <div class="photo" role="img" aria-label="Abstract molecular network backdrop" style="inset:0;background:radial-gradient(circle at 70% 30%,#2e5180,#15294a 75%)"></div>
  <div class="abs white" style="left:18px;top:95px">
    <div style="font-size:12px;font-weight:700">THANK YOU</div>
    <div style="font-size:4.5px;color:#a9c0da">For Your Precious Time</div>
  </div>
  <div class="abs" style="left:0;right:0;bottom:0;height:26px;background:#0f1f38;display:flex;align-items:center;justify-content:space-between;padding:0 8px;color:#fff;font-size:3.8px">
    <div style="display:flex;gap:4px;align-items:center"><span class="circ" style="width:6px;height:6px;background:var(--light)"></span><div><span style="color:#8ea7c4;font-size:3px">Our Address :</span><br>123 Street Name - City - 12345</div></div>
    <div style="line-height:1.8"><div style="display:flex;gap:3px;align-items:center"><span class="circ" style="width:6px;height:6px;background:var(--light)"></span>(877) 123-4567 Ext. 2</div><div style="display:flex;gap:3px;align-items:center"><span class="circ" style="width:6px;height:6px;background:var(--light)"></span>youremail@email.com</div></div>
    <div style="display:flex;gap:3px;align-items:center"><span class="circ" style="width:6px;height:6px;background:var(--light)"></span>www.veltorapharm.com</div>
  </div>
</section>

</main>
</body>
</html>
```